Jewelry shop redesign

Would like to have my webshop (www.moranti.ee) to be redesigned. The shop system, which is built in AJAX will stay the same (consists of different widgets that can be placed using html), just the surroundings needs a luxurious and clean appearance. Only things needed to keep: facebook like box, new product slideshow (can be redesigned aswell), the 3 links on the top which lead to information pages (can be made into buttons), the footer and of course the shop system widgets. The header picture/logo will need to be a link to homepage, which will be the main part of the design. I am quite keen to the display pic that i have on the fb page www.facebook.com/kiritsapood, can be used to make a logo for the header, but feel free to do whatever, as long as it is CLEAN, SIMPLE, LUXURIOUS. get rid of the calculator...

widgets to use with the design (all not needed):

Product Browser Widget Code:
<div>
<script type="text/javascript" src="http://app.shopvarn.com/script.js?718254" charset="utf-8"></script>
<script type="text/javascript"> xProductBrowser("categoriesPerRow=3","views=grid(3,3) list(10) table(20)","categoryView=grid","searchView=list","style="); </script>
<noscript>Your browser does not support JavaScript. Please proceed to <a href="http://moranti.shopvarn.com">HTML version of Moranti OÜ</a></noscript>
</div>

Bag Widget Code:
<div>
<!- remove layout parameter if you want to position minicart yourself ->
<script type="text/javascript"> xMinicart("style=","layout=attachToCategories"); </script>
</div>

minicart: 
<div> <script type="text/javascript" src="http://app.shopvarn.com/script.js?718254"></script> <script type="text/javascript"> xMinicart("style="); </script> </div>

Categories Tabs Widget Code:
<div>
<script type="text/javascript"> xCategories("style="); </script>
</div>

Categories Menu Widget Code:
<div>
<script type="text/javascript"> xVCategories("style="); </script>
</div>

Search Box Widget Code:
<div>
<script type="text/javascript"> xSearchPanel("style="); </script>
</div>

Target Market(s)

women, avg age 24

Industry/Entity Type

Shop

Requirements
Must have
• fb likebox, new product (UUED TOOTED) slideshow, keep the footer (just the company txt and pics), 3 information pages, shop widgets
Should not have
• the lease calculator.

```html
<!DOCTYPE html>
<html lang="et">
<head>
<meta charset="utf-8">
<title>Jewelry shop design</title>
<link rel="stylesheet" href="https://fonts.googleapis.com/css2?family=Tinos:ital,wght@0,400;0,700;1,400;1,700&display=swap">
<style>
  :root {
    --page: #ffffff;
    --glow: #ececec;
    --text: #505050;
    --text-dark: #444444;
    --muted: #b4b4b4;
    --rule: #cfcfcf;
    --crimson: #b5203a;
    --amber: #e98a1c;
    --footer: #dfe0e0;
    --frame: #e4e4e4;
  }
  * { margin: 0; padding: 0; box-sizing: border-box; }
  html, body { width: 1200px; height: 869px; overflow: hidden; }
  body {
    position: relative;
    background: var(--page);
    font-family: "Tinos", "Times New Roman", serif;
    color: var(--text);
  }
  .showcase {
    position: absolute; left: 0; top: 0; width: 1200px; height: 346px;
    background: radial-gradient(ellipse 640px 110px at 600px 300px, var(--glow), rgba(255,255,255,0) 100%);
  }
  .product {
    position: absolute; top: 0; width: 179px; text-align: center;
  }
  .product__photo {
    display: block; width: 179px; height: 106px;
    border: 4px solid #fff; border-top: 0;
    box-shadow: 0 0 0 1px var(--frame), 0 1px 3px rgba(0,0,0,.12);
  }
  .product__text {
    margin: 16px 12px 0; font-size: 12.5px; line-height: 17px;
  }
  .product__rule {
    width: 124px; height: 1px; background: var(--rule); margin: 6px auto 0;
  }
  .product__buy {
    display: inline-block; margin-top: 11px; font-size: 12.5px;
    font-style: italic; color: var(--muted); text-decoration: underline;
  }
  .divider {
    position: absolute; left: 219px; width: 763px; height: 1px; background: var(--rule);
  }
  .divider__ornament {
    position: absolute; left: 357px; top: -6px; width: 48px; height: 12px;
    background: #d6d6d6; border-radius: 6px;
  }
  .headline {
    position: absolute; left: 150px; top: 350px; width: 890px;
    text-align: center; font-style: italic; font-weight: 400;
    font-size: 32px; line-height: 57px; color: var(--text-dark);
  }
  .headline__accent { color: var(--crimson); font-size: 42px; }
  .intro {
    position: absolute; left: 147px; top: 483px; width: 254px;
    font-weight: 700; font-size: 12.5px; line-height: 17px;
  }
  .intro__text { width: 246px; }
  .intro__rule { height: 1px; background: var(--rule); margin-top: 6px; }
  .intro__more {
    display: block; text-align: right; margin-top: 6px;
    font-style: italic; color: var(--muted); text-decoration: underline;
  }
  .column-rule {
    position: absolute; left: 448px; top: 483px; width: 1px; height: 136px; background: var(--rule);
  }
  .point { position: absolute; left: 485px; width: 270px; }
  .point__badge {
    position: absolute; left: 0; top: 0; width: 47px; height: 47px; border-radius: 50%;
    color: #fff; font-style: italic; font-weight: 700; font-size: 16px;
    display: flex; align-items: center; justify-content: center;
  }
  .point__body {
    margin-left: 58px; font-weight: 700; font-size: 12.5px; line-height: 17px; width: 186px;
  }
  .point__title { font-style: italic; }
  .point--location { top: 486px; }
  .point--location .point__badge { background: var(--crimson); }
  .point--location .point__title { color: var(--crimson); }
  .point--info { top: 554px; }
  .point--info .point__badge { background: var(--amber); top: 1px; }
  .point--info .point__title { color: var(--amber); }
  .contact {
    position: absolute; left: 415px; top: 671px; color: var(--text-dark); font-size: 22px;
  }
  .contact__label { position: absolute; left: 0; top: 0; font-weight: 700; white-space: nowrap; }
  .contact__numbers { position: absolute; left: 189px; top: 0; line-height: 22px; white-space: nowrap; }
  .contact__numbers strong { display: block; }
  .site-footer {
    position: absolute; left: 0; top: 783px; width: 1200px; height: 86px;
    background: var(--footer); text-align: center;
    font-weight: 700; font-size: 12.5px; padding-top: 18px;
  }
</style>
</head>
<body>
  <section class="showcase">
    <article class="product" style="left:147px">
      <div class="product__photo" role="img" aria-label="Photo of a silver floral brooch with stones" style="background:linear-gradient(160deg,#4a4e49,#2f332f)"></div>
      <p class="product__text">Tellida saab ööpäevaringselt. Ostu on võimalik sooritada registreerudes või registreerimata. Registreerumiseks on vajalik vaid posti aadress ja telefoni number ning sisselogimiseks kasutajanime koos parooliga. This is a dummy text</p>
      <div class="product__rule"></div>
      <a class="product__buy">Buy Now</a>
    </article>
    <article class="product" style="left:373px">
      <div class="product__photo" role="img" aria-label="Photo of a textured metal ring" style="background:linear-gradient(180deg,#f2f2f4,#8d92ac 60%,#5b6190)"></div>
      <p class="product__text">Tellida saab ööpäevaringselt. Ostu on võimalik sooritada registreerudes või registreerimata. Registreerumiseks on vajalik vaid posti aadress ja telefoni number ning sisselogimiseks kasutajanime koos parooliga. This is a dummy text</p>
      <div class="product__rule"></div>
      <a class="product__buy">Buy now</a>
    </article>
    <article class="product" style="left:599px">
      <div class="product__photo" role="img" aria-label="Photo of a crystal necklace" style="background:linear-gradient(160deg,#c9b9a6,#a89280)"></div>
      <p class="product__text">Tellida saab ööpäevaringselt. Ostu on võimalik sooritada registreerudes või registreerimata. Registreerumiseks on vajalik vaid posti aadress ja telefoni number ning sisselogimiseks kasutajanime koos parooliga. This is a dummy text</p>
      <div class="product__rule"></div>
      <a class="product__buy">Buy Now</a>
    </article>
    <article class="product" style="left:825px">
      <div class="product__photo" role="img" aria-label="Photo of turquoise jewelry set on display stands" style="background:linear-gradient(160deg,#d8c9ad,#c4b292)"></div>
      <p class="product__text">Tellida saab ööpäevaringselt. Ostu on võimalik sooritada registreerudes või registreerimata. Registreerumiseks on vajalik vaid posti aadress ja telefoni number ning sisselogimiseks kasutajanime koos parooliga. This is a dummy text</p>
      <div class="product__rule"></div>
      <a class="product__buy">Buy Now</a>
    </article>
  </section>

  <div class="divider" style="top:346px"><span class="divider__ornament" role="img" aria-label="Small ornament"></span></div>

  <h1 class="headline"><span class="headline__accent">This will be remove!</span>After Being select our design this will be remove</h1>

  <div class="intro">
    <p class="intro__text">Tellida saab ööpäevaringselt. Ostu on võimalik sooritada registreerudes või registreerimata. Registreerumiseks on vajalik vaid posti aadress ja telefoni number ning sisselogimiseks kasutajanime koos parooliga. This is a dummy text</p>
    <div class="intro__rule"></div>
    <a class="intro__more">read more</a>
  </div>

  <div class="column-rule"></div>

  <div class="point point--location">
    <span class="point__badge">01.</span>
    <p class="point__body"><span class="point__title">Our location</span><br>Your Location will go here!</p>
  </div>
  <div class="point point--info">
    <span class="point__badge">02.</span>
    <p class="point__body"><span class="point__title">Vivamus sed arcu dui, eu tincidunt sem.</span> Vivamus hendrerit mauris ut dui gravida ut viverra tincidunt.</p>
  </div>

  <div class="divider" style="top:636px"><span class="divider__ornament" role="img" aria-label="Small ornament"></span></div>

  <div class="contact">
    <span class="contact__label">CALL US FREE:</span>
    <div class="contact__numbers"><strong>00000555010099</strong>00000555010099</div>
  </div>

  <footer class="site-footer">© 2012 Jewelry shop design</footer>
</body>
</html>
```